Kids painting app needs in-app icons

Need a set of in-app icons for a kids painting app. There are currently place-holder icons in place, but these icons are inconsistent and quite dull for a kids app.

Specifically we need 7 icons and a design for a slider.

***********************************************************************************************
See the "Nice to Haves" section below for updated comments to this brief.

We are looking for icons that are playful, but also don't want them to be overbearing, since the intent of the app is to focus on the painting experience itself, so limiting visual clutter is one of the core design goals.

We also want to avoid words as icons, since the intention is to localise the app in to a number of different languages, and we want to avoid the need to localise the icons themselves.

See the attached images for reference to the current placeholder layout. We do not what to spend too much time adjusting the current layout at present, but feel free to play around with your layout when presenting your work in place if you feel it significantly enhances the painting app overall.

You can try out the app on a recent iOS device by signing up to the alpha testing program from our web-site - www.brightmixstudios.com

Regards,
Tom

Target Market(s)

Painting app designed specifically for kids

Colors

Designer to choose colors to be used in the design.

Requirements
Must have
• The required elements are as follows:
• * Clean brush icon
• Tapping this icon will clean the paint off of the brush. This is currently being represented by the head of a brush, which we believe is quite appropriate, but if you feel there is a better way to represent this action we are open to suggestions.
• A design idea may be to have two variations of this icon: one with paint on the brush and one without paint on the brush. It would then be possible to display, or perhaps even blend between these two images to highlight the build up of paint on the brush, but primarily to highlight the purpose of the icon by giving visual feedback after pressing the icon
• * Options icon
• This is currently being represented by a gear icon. The option icon and the clean brush icon are the only two UI elements that are always visible. This icon simply shows / hides the final three additional icons
• * Share icon
• This icon is based on the standard iOS share icon, which launches the standard iOS share dialog. Any suggestions on a more kids friendly design are welcome, but feel free to include a design based off of the standard share icon if you feel it is still the most appropriate icon design to use
• * Return to Gallery
• We are currently using a green tick icon to represent this operation. Some of the thought process behind this icon was that we were also saving the image as we returned to the gallery, however saving will now happen automatically after each brush stroke, so that mental concept has been relaxed.
• * Reset Painting
• We are currently using a red X icon to represent this operation. This allows you to clear the canvas, clean the brush, and reset the paint palette all with a single icon press.
• * Undo / Redo
• While not implemented at present, we may implement undo / redo functionality in the future, so we would like icon designs for these. Also, having to include designs for undo and redo will like influence how you design the Return to Gallery icon, in order to differentiate the operations.
• There is also one more visual element that need further attention, but isn't exactly an icon:
• * Brush width slider
• After performing a long press on the clean brush icon, the brush width slider appears. This is currently using a standard iOS slider. Note that ideally this slider should not always be visible, in order to limit on-screen clutter, but it is also important for it to be easily discoverable and intuitive to use.
• Side note:
• It is straight-forward to tint any white icons inside iOS, so icons can be created in grey scale and coloured inside the app. However, if your design has a specific colour theme please provide both grey scale and full colour versions to make it easy for use to possibly offer different colour themes inside the app at a later date.
Nice to have
• ***********************************************************************************************
• UPDATE: 23 May - Consistency with logo
• Firstly, thank you to everyone who has already submitted a design. Seeing
• the variation in design makes it a lot easier for us to figure out our intended
• direction.
• I have uploaded two additional images of our P logo, and how it is integrated into the Brightmix Kids logo. Also, you may have noticed that the palette is rounded with circular paint swatches.
• We would like this rounded / circular theme to be a part of the icon designs also. This could mean having a rounded / circular background outline or rounded / circular features of the icon itself.
• Having the outline of the icons themselves appearing as if painted is something we are interested in exploring, similar to the P logo itself but probably greyscale or outlined
• Having seen a number of designs we are gravitating towards cleaner designs, either black and white or using just a single colour

```html
<!DOCTYPE html>
<html lang="en">
<head>
<meta charset="utf-8">
<title>Painting Canvas</title>
<link rel="stylesheet" href="https://fonts.googleapis.com/css2?family=Nunito:wght@600&display=swap">
<style>
  :root {
    --canvas-bg: #a4bad3;
    --button-bg: #ffffff;
    --button-shadow: rgba(60, 85, 120, 0.18);
    --accent-blue: #2a8de8;
    --menu-blue: #1a8ff0;
    --track: #ffffff;
    --knob: #2a7fd9;
    --tray-top: #c3d5f1;
    --tray-edge: #e4eefb;
    --tray-shadow: #8aa2be;
    --well-rim: #eef4fc;
    --paint-black: #0a0c18;
    --paint-red: #c4241c;
    --paint-yellow: #c7c432;
    --paint-blue: #0d2fd6;
    --paint-empty: #d7e3f4;
    --brush-handle: #e0782a;
    --brush-tip: #2f5fae;
    --share-yellow: #f2b21a;
    --share-blue: #5bb7e8;
    --share-red: #ea5a4a;
    --easel-frame: #444444;
    --easel-picture: #e8504a;
    --stack-back: #9a9a9a;
    --stack-mid: #c8c8c8;
    --stack-front: #eeeeee;
    --stack-picture: #5c7cc8;
  }
  * { box-sizing: border-box; margin: 0; padding: 0; }
  html, body { width: 1200px; height: 901px; overflow: hidden; }
  body {
    background: var(--canvas-bg);
    font-family: "Nunito", sans-serif;
    position: relative;
  }
  .tool-button {
    position: absolute;
    top: 16px;
    width: 79px;
    height: 79px;
    background: var(--button-bg);
    border-radius: 6px;
    box-shadow: 0 1px 3px var(--button-shadow);
    display: flex;
    align-items: center;
    justify-content: center;
  }
  .tool-button svg { width: 56px; height: 56px; }
  .clean-brush { left: 26px; }
  .undo-redo { left: 728px; }
  .gallery { left: 821px; }
  .reset { left: 914px; }
  .share { left: 1007px; }
  .options { left: 1100px; }

  .width-slider {
    position: absolute;
    left: 57px;
    top: 161px;
    width: 8px;
    height: 284px;
    background: var(--track);
    border-radius: 4px;
  }
  .width-slider .knob {
    position: absolute;
    left: -12px;
    top: 24px;
    width: 32px;
    height: 32px;
    border-radius: 50%;
    background: var(--knob);
  }
  .palette { position: absolute; left: 0; top: 0; }
</style>
</head>
<body>
  <svg class="palette" width="1200" height="901" viewBox="0 0 1200 901" aria-label="Paint palette">
    <g class="palette-tray" transform="translate(278 368) rotate(-50.7)">
      <rect class="tray-shadow" x="-300" y="-58" width="572" height="170" rx="58" fill="var(--tray-shadow)" transform="rotate(50.7) translate(-14 46) rotate(-50.7)"/>
      <rect x="-286" y="-58" width="572" height="116" rx="58" fill="var(--tray-top)" stroke="var(--tray-edge)" stroke-width="4"/>
      <circle cx="-228" cy="0" r="44" fill="var(--paint-black)" stroke="var(--well-rim)" stroke-width="5"/>
      <circle cx="-114" cy="0" r="44" fill="var(--paint-red)" stroke="var(--well-rim)" stroke-width="5"/>
      <circle cx="0" cy="0" r="44" fill="var(--paint-yellow)" stroke="var(--well-rim)" stroke-width="5"/>
      <circle cx="114" cy="0" r="44" fill="var(--paint-blue)" stroke="var(--well-rim)" stroke-width="5"/>
      <circle cx="228" cy="0" r="44" fill="var(--paint-empty)" stroke="var(--well-rim)" stroke-width="5"/>
    </g>
  </svg>

  <div class="tool-button clean-brush" aria-label="Clean brush">
    <svg viewBox="0 0 56 56">
      <path d="M46 6 L52 12 L28 32 L24 28 Z" fill="var(--brush-handle)"/>
      <path d="M22 30 L26 34 Q22 46 8 50 Q12 36 22 30 Z" fill="var(--brush-tip)"/>
    </svg>
  </div>
  <div class="tool-button undo-redo" aria-label="Undo and redo">
    <svg viewBox="0 0 56 56">
      <g class="undo">
        <path d="M27 36 C27 27 22 22 15 24" fill="none" stroke="var(--accent-blue)" stroke-width="5" stroke-linecap="round"/>
        <polygon points="4,27 17,16 19,32" fill="var(--accent-blue)"/>
      </g>
      <g class="redo">
        <path d="M29 36 C29 27 34 22 41 24" fill="none" stroke="var(--accent-blue)" stroke-width="5" stroke-linecap="round"/>
        <polygon points="52,27 39,16 37,32" fill="var(--accent-blue)"/>
      </g>
    </svg>
  </div>
  <div class="tool-button gallery" aria-label="Return to gallery">
    <svg viewBox="0 0 56 56">
      <rect x="4" y="12" width="30" height="22" fill="#f2f2f2" stroke="var(--easel-frame)" stroke-width="2"/>
      <rect x="8" y="16" width="22" height="14" fill="var(--easel-picture)"/>
      <path d="M12 34 L8 48 M26 34 L30 48" stroke="var(--easel-frame)" stroke-width="3"/>
      <path d="M38 26 Q50 22 50 34 Q50 42 40 42 M40 36 L38 43 L45 45" fill="none" stroke="var(--share-blue)" stroke-width="4" stroke-linecap="round"/>
    </svg>
  </div>
  <div class="tool-button reset" aria-label="Reset painting">
    <svg viewBox="0 0 56 56">
      <rect x="14" y="14" width="32" height="36" rx="2" fill="var(--stack-back)"/>
      <rect x="10" y="10" width="32" height="36" rx="2" fill="var(--stack-mid)"/>
      <rect x="6" y="6" width="32" height="36" rx="2" fill="var(--stack-front)" stroke="var(--stack-back)" stroke-width="1.5"/>
      <rect x="12" y="14" width="20" height="20" fill="var(--stack-picture)"/>
    </svg>
  </div>
  <div class="tool-button share" aria-label="Share">
    <svg viewBox="0 0 56 56" fill="none" stroke-width="5">
      <path d="M16 28 L40 14 M16 28 L40 42" stroke="#7c8da6" stroke-width="3"/>
      <circle cx="14" cy="28" r="8" stroke="var(--share-yellow)"/>
      <circle cx="42" cy="12" r="8" stroke="var(--share-blue)"/>
      <circle cx="42" cy="44" r="8" stroke="var(--share-red)"/>
    </svg>
  </div>
  <div class="tool-button options" aria-label="Options">
    <svg viewBox="0 0 56 56">
      <rect x="6" y="6" width="44" height="44" rx="12" fill="var(--menu-blue)"/>
      <path d="M19 20 H37 M19 28 H37 M19 36 H37" stroke="#ffffff" stroke-width="2.5" stroke-linecap="round"/>
    </svg>
  </div>

  <div class="width-slider" aria-label="Brush width">
    <div class="knob"></div>
  </div>
</body>
</html>
```